Postcard to Market Greeting Cards

Need a Postcard to
* Promote a particular human being and his story.
* Market and raise awareness of his art
* Advertise his website where the art can be purchased.

Background:
Davor Kelmandi is a refugee and artist trapped in a refugee camp in Indonesia.
He has committed no crimes. He had to escape his country as a refugee.
He is currently held in detention. The only way out is to be privately sponsored.
This costs a huge amount of money. Davor is working to raise the money needed.
He is young and has lost 5 years being imprisoned. We must work to save him.

He draws everyday and sends the drawings to me. I make them into beautiful hand drawn art cards which we sell at markets, on the internet or via contacts.
He is not allowed to work. Secret drawing is the only way he can make a living.

This postcard is to
* share some of Davor's Story and to give a sense of who he is.
* display his beautiful art cards which are sold for income via his website.
* Prominently display his website address as well as images of the cards.

These postcards will be given out at markets, letterbox dropped, sent to new customers, left in cafes and libraries etc so people will discover Davor's Cards....
By buying the cards...Davor can earn the funds he needs to pay for sponsorship into a free country. Many countries will accept him if he pays for the process.

Therefore...the postcard needs to be filled front and back. No need to leave space for address and postage. This leaves more room for samples of the Greeting Cards.

There is text provided for the front and back of the POSTCARD.
This may be edited and added to as the design process continues.

Images of Davor's Cards have been uploaded for you.
It would be great if these can be beautifully and artistically presented on the postcard. The aim is to attract people to Davor's hand drawn cards motivate people to want to buy them. Not all of the card images need to be used.

There are * black line cards * colour cards. * framed colour art works
so some of each could be promoted on the postcard.

Davor's Story will be included on the back of the card labelled for the Back.
A few words will be clearly and displayed on the front. Labelled fo the front.

The front art can be a single drawing image from Davor OR a collage of many OR
It can contain his image or a few small images. See what you feel works well as there is scope to create a BEAUTIFUL postcard that depicts beautiful CARDS.

There is a quote from Davor to be included on the front.
Can it be written in a handwriting style font to make it look like Davor has written the message himself ?

There are images of Davor to be used on the front and back.
Davor's images have ben taken on dodgy phones and may not be a good quality.
They don't need to be large images and they DON'T need to all be used. There is a selection to choose from.

Davor is in a prison. Maybe there are design elements that might remind of this.
Barbed wire maybe. Fences. The over all feel though is FREEDOM and BEAUTY in the hand drawn art cards and the escape they will provide in the end.

Davor's website to be displayed on the front and back
davorsketch.net

email address on the back
helpdavor2031@mailpost.net

These postcards will encourage buyers to read Davor's Story and want to help.
They will display beautifully hand drawn art cards which people will want to buy.
They will display the website address prominently and in some clever. arty way.

Good luck with it all.
I plan to increase first prize money depending on the designs....
and to offer more than first place depending on the deigns.

Please feel free to ask me any questions at any time.

Good luck and thanks for considering this project.

Neil Farrow

Target Market(s)

Broad human rights supporters who will enjoy seeing a human story and will want to. respond.

Industry/Entity Type

Human Rights

Colors

Designer to choose colors to be used in the design.

Requirements
Must have
• Colourful and imaginative way of displaying the Greeting Cards being marketed by the Postcard. It is a taster and a sampling. They do not need to be arranged in rows or order..better to be creative in displaying the samples of cards. The website has the organised online shop. The postcard is a sampler and should MAKE people want to go to the website to buy the cards. The postcard must share the story of the artist.
• Handwriting font for the quote from the artist to make it look like he has written a personal message.
• Postcard needs to be filled on front and back. No blank space for mailing and address.
Nice to have
• Free and easy arty design. Photograph of the artist placed in some creative way.
Should not have
• Conservative structure. Free and arty is better.
• The postcard needs to be filled on the front and back ! No need to leave the bank area for mailing as it will only be used for marketing and distribution. it won't actually be used for mailing.

```html
<!DOCTYPE html>
<html lang="en">
<head>
<meta charset="utf-8">
<title>Free Davor – Postcard Front and Back</title>
<link rel="stylesheet" href="https://fonts.googleapis.com/css2?family=Dancing+Script:wght@500&family=Mrs+Saint+Delafield&family=Open+Sans:ital,wght@0,400;0,600;0,700;1,400&family=Oswald:wght@300;400&family=Playfair+Display:wght@400&family=Roboto:wght@500&display=swap">
<style>
  :root {
    --page: #e4e4e4;
    --frame: #6a5423;
    --panel-top: #2d2f20;
    --panel-bottom: #141510;
    --wood-light: #5a3a24;
    --wood-dark: #2a1a10;
    --gold-light: #f6c640;
    --gold-mid: #d99a16;
    --gold-dark: #9c6408;
    --maroon: #6b2b1a;
    --ink-light: #f2efe6;
    --accent-yellow: #f2c230;
    --site-orange: #f3a23a;
    --line-grey: #9a9a9a;
    --white: #ffffff;
  }
  * { box-sizing: border-box; margin: 0; padding: 0; }
  html, body {
    width: 991px; height: 1200px; overflow: hidden;
    background: var(--page);
  }
  .postcard {
    position: absolute; left: 135px;
    width: 720px; height: 555px;
    background: var(--frame);
    box-shadow: 0 6px 14px rgba(0,0,0,.25);
  }
  .postcard--front { top: 30px; }
  .postcard--back { top: 615px; }

  .dark-panel {
    position: absolute;
    background: linear-gradient(180deg, var(--panel-top), var(--panel-bottom));
  }
  .wood-band {
    position: absolute;
    background: linear-gradient(180deg, var(--wood-light), var(--wood-dark) 55%, var(--wood-light));
  }
  .site-name {
    position: absolute; text-align: center;
    font-family: "Oswald", sans-serif; font-weight: 300;
    text-transform: uppercase; letter-spacing: 2px;
    color: var(--site-orange);
  }

  /* Front */
  .front-panel { left: 18px; top: 18px; width: 364px; height: 443px; }
  .title-lettering {
    position: absolute; left: 40px; top: 30px; width: 292px; height: 112px;
    border-radius: 40px;
    background: linear-gradient(100deg, #f4a21c 0%, #e0457a 45%, #b53fd0 70%, #4b6ce0 100%);
    opacity: .85;
  }
  .gold-band {
    position: absolute;
    background: linear-gradient(100deg, var(--gold-dark), var(--gold-light) 35%, var(--gold-mid) 70%, var(--gold-dark));
    display: flex; flex-direction: column; justify-content: center; align-items: center;
    text-align: center;
  }
  .front-band { left: 24px; top: 152px; width: 316px; height: 68px; }
  .front-band p {
    font-family: "Open Sans", sans-serif; font-weight: 600;
    font-size: 12.5px; line-height: 1.3; color: var(--maroon);
  }
  .quote-mark {
    position: absolute; left: 0; width: 364px; top: 214px;
    text-align: center; font-family: "Playfair Display", serif;
    font-size: 72px; line-height: 1; color: #4a4528;
  }
  .quote-box {
    position: absolute; left: 10px; top: 258px; width: 342px; height: 108px;
    border: 1px solid #5d5838;
    padding: 14px 14px 0; text-align: center;
  }
  .quote-text {
    font-family: "Dancing Script", cursive; font-size: 12.5px;
    line-height: 1.35; color: var(--ink-light);
  }
  .quote-signature {
    font-family: "Mrs Saint Delafield", cursive; font-size: 24px;
    color: var(--gold-light); margin-top: 2px;
  }
  .front-call {
    position: absolute; left: 0; top: 384px; width: 364px;
    text-align: center; font-family: "Playfair Display", serif;
    font-size: 14.5px; line-height: 1.3; color: var(--ink-light);
  }
  .front-wood { left: 18px; top: 461px; width: 684px; height: 76px; }
  .front-site { left: 18px; top: 476px; width: 364px; font-size: 36px; line-height: 46px; }
  .feature-art {
    position: absolute; left: 392px; top: 18px; width: 310px; height: 388px;
    background: radial-gradient(circle at 50% 50%, #f08a2a 0%, #f4a15a 28%, #f1cfc0 55%, #f4ddd6 100%);
  }
  .card-sample {
    position: absolute; top: 409px; width: 105px; height: 102px;
    border: 5px solid var(--frame);
  }
  .card-sample--bird { left: 358px; background: linear-gradient(160deg, #f3f0e6, #e4dfcf); }
  .card-sample--lineflower { left: 480px; background: linear-gradient(160deg, #e2e2e2, #c7c7c7); }
  .card-sample--hummingbird { left: 602px; width: 100px; background: linear-gradient(160deg, #f4efe6, #e6c8b8); }

  /* Back */
  .back-panel { left: 18px; top: 18px; width: 326px; height: 443px; }
  .artist-photo {
    position: absolute; left: 17px; top: 17px; width: 114px; height: 136px;
    background: linear-gradient(170deg, #c9a68c, #8a6a57 60%, #e8e4e0);
    border: 2px solid var(--frame);
  }
  .story {
    position: absolute; font-family: "Open Sans", sans-serif; font-style: italic;
    font-size: 7.6px; line-height: 1.32; color: var(--ink-light); text-align: justify;
  }
  .story p + p { margin-top: 7px; }
  .story-intro { left: 130px; top: 6px; width: 176px; }
  .story-main { left: 8px; top: 148px; width: 310px; }
  .story-name { color: var(--accent-yellow); }
  .back-band { left: 14px; top: 368px; width: 298px; height: 52px; }
  .back-band p {
    font-family: "Open Sans", sans-serif; font-weight: 700;
    font-size: 7.4px; line-height: 1.45; color: var(--maroon);
  }
  .back-wood { left: 18px; top: 461px; width: 326px; height: 76px; }
  .back-site { left: 18px; top: 462px; width: 326px; font-size: 34px; line-height: 44px; }
  .back-email {
    position: absolute; left: 18px; top: 508px; width: 326px; text-align: center;
    font-family: "Open Sans", sans-serif; font-style: italic;
    font-size: 13px; color: var(--white);
  }
  .address-side {
    position: absolute; left: 344px; top: 0; width: 376px; height: 555px;
    background: var(--white);
  }
  .stamp-box {
    position: absolute; left: 226px; top: 33px; width: 109px; height: 131px;
    border: 1px solid var(--line-grey);
    display: flex; align-items: center; justify-content: center; text-align: center;
    font-family: "Roboto", sans-serif; font-weight: 500; font-size: 13px;
    line-height: 1.3; color: #333;
  }
  .address-line {
    position: absolute; left: 73px; width: 262px; height: 0;
    border-top: 1px solid var(--line-grey);
  }
</style>
</head>
<body>

<section class="postcard postcard--front" aria-label="Postcard front">
  <div class="dark-panel front-panel">
    <div class="title-lettering" role="img" aria-label="Colourful hand lettering reading Free Davor"></div>
    <div class="gold-band front-band">
      <p>Buy Davor's Beautiful Art Cards</p>
      <p>Support Him Help Davor Pay For</p>
      <p>His Sponsorship to Freedom</p>
    </div>
    <div class="quote-mark">&ldquo;</div>
    <blockquote class="quote-box">
      <p class="quote-text">"It's true that my body is prisoner.... But my thoughts and my heart are not prisoner. No one can imprison my thoughts and my heart. Because my thoughts and my heart are with those who I love them"</p>
      <p class="quote-signature">Davor Kelmandi</p>
    </blockquote>
    <p class="front-call">Read Davor's Story and Buy His Beautiful<br>Hand Drawn Art Cards. Help Save A Life</p>
  </div>
  <div class="wood-band front-wood"></div>
  <p class="site-name front-site">davorsketch.net</p>
  <div class="feature-art" role="img" aria-label="Hand drawn orange lily with green leaves on a pale pink card"></div>
  <div class="card-sample card-sample--bird" role="img" aria-label="Colour card of a yellow and black bird on a branch"></div>
  <div class="card-sample card-sample--lineflower" role="img" aria-label="Black line drawing card of flowers"></div>
  <div class="card-sample card-sample--hummingbird" role="img" aria-label="Colour card of a hummingbird and red flower"></div>
</section>

<section class="postcard postcard--back" aria-label="Postcard back">
  <div class="dark-panel back-panel">
    <div class="artist-photo" role="img" aria-label="Photograph of the artist Davor Kelmandi"></div>
    <div class="story story-intro">
      <p><span class="story-name">Davor Kelmandi</span>, a young Hazara man from Afghanistan, has been illegally held captive in an Indonesian Detention Centre for more than four years. He is a Refugee and prisoner without any crime.</p>
      <p>The Hazara are a ruthlessly persecuted people. Davor is alone in the world and bravely escaped his country to begin a new free life never expecting to be imprisoned and detained for years.</p>
    </div>
    <div class="story story-main">
      <p>An artist and photographer Davor is now a passionate Human Rights Defender. He refuses to allow his free spirit and creative nature to be dampened or imprisoned. He draws sunny delicate flowers and peaceful fragile birds which sing of freedom.</p>
      <p>Davor makes his art to maintain his sanity and to encourage all who struggle for freedom to reach out and grab it with both hands. He draws daily to remind himself that what is important inside him can never be locked away. Davor wastes no time being a prisoner. He is too busy dreaming free. His art expresses that.</p>
      <p>The only escape for Davor is to be sponsored to a free country. It costs many thousands to be sponsored. Davor needs your help. He's not asking for favours or charity. He is working daily for this.</p>
      <p>Davor's daily drawings have become individual greeting cards and his beautiful, unique cards are now for sale to fund his freedom. Buy Davor's Greeting Cards so he can pay his own way to freedom.</p>
    </div>
    <div class="gold-band back-band">
      <p>Individual Cards. Sets of Cards. Stunning Framed Art Works.</p>
      <p>Beautiful black line drawing cards and full colour cards available.</p>
      <p>Davor's Cards, Art and Designs are available from</p>
    </div>
  </div>
  <div class="wood-band back-wood"></div>
  <p class="site-name back-site">davorsketch.net</p>
  <p class="back-email">helpdavor2031@mailpost.net</p>
  <div class="address-side">
    <div class="stamp-box">POSTAL<br>STAMP</div>
    <div class="address-line" style="top:232px"></div>
    <div class="address-line" style="top:292px"></div>
    <div class="address-line" style="top:345px"></div>
    <div class="address-line" style="top:406px"></div>
  </div>
</section>

</body>
</html>
```